Kitchen and Bathroom Remodeling Flyer

This flyer is for a home remodeling company that remodels peoples kitchens and bathrooms.

We want a flyer to be sophisticated: nice professional design with classy font.

FRONT OF FLYER:

I have attached the front flyer I created and there is no design to it. The reason is so you can see what text elements we want on the flyer. a second attachment has the text for easy copy and paste.

I like the idea of mentioning “Owners live in Ahwatukee” because this flyer will be passed around door to door in that town of Ahwatukee.

Please use the image and the corresponding headline specific to that image. The headline can be in the image or to the top of the image.

BACK OF FLYER:
The back of flyer is essentially a written letter with a profile image of our owners and then two testimonials at bottom. I’d like to add a little bit of design to the back of the flyer. See attachment for pdf of current text and basic structure.

Our brand colors are gray and blue# 0000cc

Our website is https://Kelmbrookrenovating.com

Thank you,
Tobias

Target Market(s)

Mostly woman. Homeowners making 100k+ a year that want to remodel their kitchen or bathroom

Industry/Entity Type

Home Improvement

Font styles to use
Serif
Sans Serif
Decorative

Colors

Designer to choose colors to be used in the design.

Requirements
Must have
• This has to be in photoshop with each element editable (I’ll want to change things down the road)
Nice to have
• Examples that I don’t want copied but so you have a rough idea of some design structure that I like:
• https://flyer.pixelvantyard.com/contest.aspx?id=5190362
• https://flyer.pixelvantyard.com/contest.aspx?id=627053
• https://flyer.pixelvantyard.com/contest.aspx?id=8831475
• https://www.pixelvantyard.com/design/42957018
• https://www.pixelvantyard.com/design/7160243
Should not have
• Nothing silly or too loud. Thank you

```html
<!DOCTYPE html>
<html lang="en">
<head>
<meta charset="utf-8">
<title>Kelmbrook Renovating – Door-to-Door Flyer</title>
<link href="https://fonts.googleapis.com/css2?family=Open+Sans:wght@400;600;700;800&family=Roboto+Condensed:wght@700&display=swap" rel="stylesheet">
<style>
  :root{
    --navy:#163a6b;
    --sky:#1e8ad6;
    --ink:#4a4f57;
    --ink-soft:#7a8089;
    --paper:#ffffff;
    --stage:#e9e8e5;
  }
  *{margin:0;padding:0;box-sizing:border-box}
  html,body{width:1200px;height:801px;overflow:hidden}
  body{background:var(--stage);font-family:"Open Sans",Arial,sans-serif;color:var(--ink);position:relative}
  .page{position:absolute;top:64px;width:520px;height:673px;background:var(--paper);overflow:hidden;box-shadow:0 6px 18px rgba(0,0,0,.18)}
  .page--front{left:50px}
  .page--back{left:630px}
  .page__shapes{position:absolute;inset:0}
  .abs{position:absolute}

  /* front */
  .headline{top:26px;left:175px;width:330px;text-align:right;color:#fff;font-family:"Roboto Condensed",Arial,sans-serif;line-height:1.1}
  .headline__main{font-size:26px;letter-spacing:.5px}
  .headline__sub{font-size:16px;letter-spacing:.8px}
  .brand{top:108px;left:22px;display:flex;align-items:center;gap:8px}
  .brand__mark{width:14px;height:14px;background:var(--navy)}
  .brand__name{font-size:15px;font-weight:700;color:var(--navy)}
  .feature-band{top:425px;left:70px;width:438px;color:#fff;font-family:"Roboto Condensed",Arial,sans-serif;font-size:13px;line-height:16px;text-align:right;letter-spacing:.2px;white-space:nowrap}
  .contact{top:466px;left:300px;width:205px;color:var(--navy)}
  .contact__name{font-family:"Roboto Condensed",Arial,sans-serif;font-size:14px;color:var(--sky)}
  .contact__phone{font-size:15px;font-weight:800;margin-top:3px}
  .contact__url{font-size:11px;color:var(--ink)}
  .contact__cred{font-size:11px;font-weight:700;letter-spacing:.4px}
  .promises-title{top:500px;left:18px;color:#fff;font-family:"Roboto Condensed",Arial,sans-serif;font-size:15px;line-height:20px;letter-spacing:.5px}
  .promises{top:532px;left:22px;list-style:none;font-size:11.5px;line-height:17px;color:var(--ink)}
  .promises li::before{content:"";display:inline-block;width:5px;height:5px;border-radius:50%;background:var(--navy);margin:0 8px 2px 0}

  /* back */
  .salutation{top:106px;left:22px;color:#fff;font-size:12.5px;font-weight:700}
  .letter{top:140px;left:26px;width:468px;font-size:8.6px;line-height:1.45;color:var(--ink-soft)}
  .letter p{margin-bottom:7px}
  .letter__close{font-size:11px;font-weight:700;color:var(--ink);margin-top:4px}
  .signature{top:372px;left:26px;color:var(--navy)}
  .signature__names{font-size:15px;font-weight:800;color:var(--sky)}
  .signature__line{font-size:9.5px;color:var(--ink)}
  .signature__phone{font-size:19px;font-weight:800;margin-top:3px}
  .owner-photo{top:358px;left:292px;width:202px;height:96px;background:linear-gradient(135deg,#2b2f35,#15181c)}
  .quote{font-size:8.4px;line-height:1.45;color:var(--ink-soft)}
  .quote__mark{font-family:Georgia,serif;font-size:28px;line-height:1;color:var(--ink)}
  .reviewer{font-size:8px;font-weight:700;color:var(--ink);text-align:center;width:70px}
</style>
</head>
<body>

<section class="page page--front">
  <svg class="page__shapes" width="520" height="673" viewBox="0 0 520 673">
    <defs>
      <linearGradient id="fBath" x1="0" y1="0" x2="1" y2="1"><stop offset="0" stop-color="#9aa0a6"/><stop offset="1" stop-color="#5f656c"/></linearGradient>
      <linearGradient id="fKitchen" x1="0" y1="0" x2="1" y2="1"><stop offset="0" stop-color="#e4e6e9"/><stop offset="1" stop-color="#9ea4ab"/></linearGradient>
      <linearGradient id="fKitchen2" x1="0" y1="0" x2="1" y2="1"><stop offset="0" stop-color="#d6d9dc"/><stop offset="1" stop-color="#7d838a"/></linearGradient>
    </defs>
    <polygon points="215,96 520,96 520,420 100,420 160,310" fill="url(#fKitchen)" stroke="#fff" stroke-width="6" role="img" aria-label="Photo of a bright stainless steel kitchen with island"/>
    <polygon points="0,150 220,150 155,305 0,345" fill="url(#fBath)" stroke="#fff" stroke-width="6" role="img" aria-label="Photo of a modern bathroom with mosaic tile wall"/>
    <polygon points="0,352 155,312 100,420 260,420 0,470" fill="url(#fKitchen2)" stroke="#fff" stroke-width="6" role="img" aria-label="Photo of a white kitchen with marble table"/>
    <polygon points="0,345 160,308 163,316 0,356" fill="var(--sky)"/>
    <polygon points="170,18 520,18 520,90 140,90" fill="var(--navy)"/>
    <polygon points="140,92 520,92 520,98 137,98" fill="var(--sky)"/>
    <polygon points="0,140 200,140 195,146 0,146" fill="var(--navy)"/>
    <polygon points="82,418 520,418 520,446 60,446" fill="var(--navy)"/>
    <polygon points="58,450 520,450 520,455 55,455" fill="var(--sky)"/>
    <polygon points="0,496 240,496 215,524 0,524" fill="var(--navy)"/>
    <polygon points="0,655 360,655 390,640 520,640 520,673 0,673" fill="var(--navy)"/>
    <polygon points="380,632 520,632 520,637 375,637" fill="var(--sky)"/>
  </svg>

  <h1 class="abs headline">
    <div class="headline__main">TURN AN OLD BATHROOM</div>
    <div class="headline__sub">INTO YOUR OWN PERSONAL SPA</div>
  </h1>
  <div class="abs brand"><span class="brand__mark"></span><span class="brand__name">Kelmbrook Renovating</span></div>
  <div class="abs feature-band">ENTERTAIN IN A KITCHEN YOU'LL LOVE SHOWING OFF TO FRIENDS &amp; FAMILY</div>

  <div class="abs contact">
    <div class="contact__name">KELMBROOK RENOVATING</div>
    <div class="contact__phone">480-555-0173 ROC# 274519</div>
    <div class="contact__url">Kelmbrookrenovating.com</div>
    <div class="contact__cred">LICENSED | BONDED | INSURED</div>
  </div>

  <h2 class="abs promises-title">OUR CLIENT PROMISES:</h2>
  <ul class="abs promises">
    <li>Provide honest and straight forward advice</li>
    <li>Return calls and show up on time</li>
    <li>Employ professional, respectful and knowledgeable employees</li>
    <li>Respect your home and ensure we keep it clean</li>
    <li>Provide clear expectations of project timelines and pricing</li>
    <li>Create your dream living space with great attention to detail</li>
  </ul>
</section>

<section class="page page--back">
  <svg class="page__shapes" width="520" height="673" viewBox="0 0 520 673">
    <defs>
      <linearGradient id="bTop" x1="0" y1="0" x2="1" y2="1"><stop offset="0" stop-color="#d9dcdf"/><stop offset="1" stop-color="#868c93"/></linearGradient>
    </defs>
    <polygon points="0,0 520,0 520,40 0,95" fill="url(#bTop)" role="img" aria-label="Photo of a modern open kitchen and living space"/>
    <polygon points="0,95 520,40 520,52 0,108" fill="var(--sky)"/>
    <polygon points="0,100 240,100 220,126 0,126" fill="var(--navy)"/>
    <circle cx="320" cy="515" r="22" fill="#1c1f23" role="img" aria-label="Portrait of reviewers Lena and Hugo"/>
    <circle cx="52" cy="592" r="22" fill="#1c1f23" role="img" aria-label="Portrait of reviewers Marisa and Paul"/>
    <polygon points="0,655 360,655 390,640 520,640 520,673 0,673" fill="var(--navy)"/>
    <polygon points="380,632 520,632 520,637 375,637" fill="var(--sky)"/>
  </svg>

  <div class="abs salutation">Dear Ahwatukee Homeowners,</div>
  <div class="abs letter">
    <p>Everyone wants a dream home they can be proud of. We all want to feel welcome in life and your home is an extension of yourself, your style and your success.</p>
    <p>We understand working with a remodeling contractor can be frustrating because they show up late, change the price and make a mess of your home.</p>
    <p>Kelmbrook Renovating is the most organized remodeling company in the valley and we will create the dream space you'll be proud to show off to your friends, family and neighbors.</p>
    <p>One of our co-founders, Tobias, has been through several contractor nightmares, and it is the main reason Tobias, Owen and Silas started Kelmbrook Renovating.</p>
    <p>We are an award-winning home remodeling licensed contractor known for showing up on time, being organized, clearly explaining all aspects of the remodel and adhering to project budget and timeline.</p>
    <p>One of our clients said we were the calmest part of their remodel. We'll guide you through our simple process and there is no haggle, no sales tricks and our clients love the experience.</p>
    <p class="letter__close">To a beautiful home you'll love showing off to your neighbors, family &amp; friends,</p>
  </div>
  <div class="abs signature">
    <div class="signature__names">Tobias, Owen and Silas</div>
    <div class="signature__line">Kelmbrook Renovating</div>
    <div class="signature__line">ROC# 274519</div>
    <div class="signature__line">Kelmbrookrenovating.com</div>
    <div class="signature__phone">480-555-0173</div>
  </div>
  <div class="abs owner-photo" role="img" aria-label="Photo of the owners Tobias, Owen and Silas"></div>

  <div class="abs quote__mark" style="top:468px;left:352px">&ldquo;</div>
  <div class="abs quote" style="top:482px;left:352px;width:145px">
    <p>Our bathroom is amazing. The crew was always easy to work with and they kept our house clean.</p>
    <p style="margin-top:5px">I would hire them again for any project in our home. We will be calling them soon. Thank you!</p>
  </div>
  <div class="abs quote__mark" style="top:556px;left:478px">&rdquo;</div>
  <div class="abs reviewer" style="top:540px;left:285px">Lena and Hugo</div>

  <div class="abs quote__mark" style="top:548px;left:86px">&ldquo;</div>
  <div class="abs quote" style="top:562px;left:86px;width:150px">
    <p>The team was easy to work with and their attention to detail was truly great.</p>
    <p style="margin-top:5px">Our kitchen looks perfect and we love it. We could not be happier. Thanks, Kelmbrook Renovating.</p>
  </div>
  <div class="abs reviewer" style="top:618px;left:17px">Marisa &amp; Paul T.</div>
</section>

</body>
</html>
```